Nail Technician Business Card Design

My business is a nail technician business which involves applying nail enhancements to clients nails. I would like a design that uses the colours:, purple or black and silver on a light grey background. The final design should entice clients to my business.
I would like appointment times on the back of the card.
I want the spilled bottle on the front and the other one on the back
I would like the dragonfly font
Updates
Reason: I have found a font I would like used and also an image/logo
I have listed some ideas I would like used on the design of my card. thanks
Petra
Industry/Entity Type
Business
Contact Information for Business Card
Lumira Nail Designs
47 Wexcombe street,
Yarrowdale, QLD 2851
Mobile: 0400 582 316
Petra Hawkins
Like us on Facebook
Font styles to use
Other font styles liked:
- Dragonfly
Look and feel
Each slider illustrates characteristics of the customer's brand and the style your logo design should communicate.

```html
<!DOCTYPE html>
<html lang="en">
<head>
<meta charset="utf-8">
<title>Lumira Nail Designs – Business Card</title>
<link rel="stylesheet" href="https://fonts.googleapis.com/css2?family=Cinzel:wght@400;600&family=Libre+Baskerville&family=Open+Sans:wght@700&display=swap">
<style>
  :root {
    --page-bg: #f2f2f3;
    --card-purple: #2a0944;
    --band-grey: #474548;
    --magenta-glow: #a81f8f;
    --purple-deep: #3d0b57;
    --silver: #e4e4e8;
    --silver-soft: #b9b8c0;
    --label-grey: #b3b2b8;
  }
  * { margin: 0; padding: 0; box-sizing: border-box; }
  html, body {
    width: 1200px; height: 1000px; overflow: hidden;
    background: var(--page-bg);
  }
  .canvas {
    position: relative; width: 1200px; height: 1000px;
    display: flex; flex-direction: column; align-items: center;
    justify-content: center; gap: 36px;
  }
  .card {
    position: relative; width: 800px; height: 457px; overflow: hidden;
    box-shadow: 0 10px 28px rgba(0,0,0,0.28);
  }

  /* Front: contact side */
  .card-front { background: var(--card-purple); }
  .card-front .top-band {
    position: absolute; left: 0; top: 0; width: 100%; height: 230px;
  }
  .card-front .identity {
    position: absolute; top: 82px; left: 0; width: 100%; text-align: center;
  }
  .identity .person-name {
    font-family: "Cinzel", serif; font-weight: 400;
    font-size: 40px; color: #ffffff; letter-spacing: 1px;
  }
  .identity .person-role {
    font-family: "Cinzel", serif; font-weight: 400; font-size: 24px;
    color: var(--silver-soft); letter-spacing: 1.5px; margin-top: 2px;
  }
  .contact-list {
    position: absolute; left: 200px; top: 270px; list-style: none;
  }
  .contact-list li {
    display: flex; align-items: baseline; margin-bottom: 24px;
  }
  .contact-list .label {
    font-family: "Open Sans", sans-serif; font-weight: 700;
    font-size: 21px; color: var(--label-grey); width: 46px;
  }
  .contact-list .colon {
    font-family: "Libre Baskerville", serif; color: var(--silver);
    font-size: 20px; width: 30px; text-align: center;
  }
  .contact-list .value {
    font-family: "Libre Baskerville", serif; font-size: 20px; color: #f4f2f6;
    white-space: nowrap;
  }

  /* Back: brand side */
  .card-back {
    background: radial-gradient(ellipse 60% 75% at 50% 50%, var(--magenta-glow) 0%, #6e1679 45%, var(--purple-deep) 100%);
  }
  .ornament-area {
    position: absolute; left: 130px; top: 95px; width: 540px; height: 270px;
    border-radius: 50%;
    background: radial-gradient(ellipse at center, rgba(138,86,184,0.35) 0%, rgba(138,86,184,0.12) 60%, rgba(138,86,184,0) 75%);
  }
  .brand-block {
    position: absolute; left: 0; top: 0; width: 100%; height: 100%;
    display: flex; flex-direction: column; align-items: center; justify-content: center;
  }
  .brand-rule {
    width: 330px; height: 1px; background: var(--silver-soft);
  }
  .brand-name {
    font-family: "Cinzel", serif; font-weight: 600; font-size: 50px;
    color: var(--silver); letter-spacing: 2px; margin: 22px 0;
    white-space: nowrap;
  }
  .social {
    position: absolute; right: 36px; top: 24px;
    display: flex; flex-direction: column; align-items: center; gap: 6px;
  }
  .social .mark {
    width: 34px; height: 34px; background: #ffffff; border-radius: 4px;
  }
  .social .hint {
    font-family: "Open Sans", sans-serif; font-weight: 700;
    font-size: 10px; color: #ffffff;
  }
</style>
</head>
<body>
<main class="canvas">

  <section class="card card-front" aria-label="Business card front">
    <svg class="top-band" viewBox="0 0 800 230" preserveAspectRatio="none" aria-hidden="true">
      <path d="M0 0 H800 V120 Q560 250 260 212 Q90 190 0 150 Z" fill="var(--band-grey)"/>
    </svg>
    <div class="identity">
      <h1 class="person-name">Petra Hawkins</h1>
      <p class="person-role">Nail Specialist</p>
    </div>
    <ul class="contact-list">
      <li><span class="label">[P]</span><span class="colon">:</span><span class="value">47 Wexcombe street, Yarrowdale, QLD 2851</span></li>
      <li><span class="label">[M]</span><span class="colon">:</span><span class="value">0400 582 316</span></li>
      <li><span class="label">[E]</span><span class="colon">:</span><span class="value">info@lumiranail.com</span></li>
    </ul>
  </section>

  <section class="card card-back" aria-label="Business card back">
    <div class="ornament-area" role="img" aria-label="Decorative purple swirl flourishes framing the brand name"></div>
    <div class="brand-block">
      <span class="brand-rule"></span>
      <h2 class="brand-name">Lumira Nail Designs</h2>
      <span class="brand-rule"></span>
    </div>
    <div class="social">
      <span class="mark"></span>
      <span class="hint">Like us</span>
    </div>
  </section>

</main>
</body>
</html>
```